Guiding Your Revenue Overhaul *

Bold eye-catching design for business non-fiction: I am seeking a bold, and clean design for a book. The book will be 6X9 for both the ebook and in print. I am open to ideas, but found that books like “steady as rain” with contrast are highly desirable for business books.

I am open to color choices.

I would also like a growth orientated graphic in the book - something to show growth, leadership, movement. Not just a plain graphic.

The title:

Guiding Your Revenue Overhaul

The subtitle - I am open to suggestions. Two subtitles I am considering:

A framework for new sales leaders and those who want to keep winning.

A guide for new sales leaders and those who want to keep winning.

The below is an introduction of the book: (Back Jacket)

Sales transformation is a topic that is infrequently written about. For the new sales leader, there are a myriad of books written on coaching, leadership, forecasting, solution selling and sales process but very little is written about how to assess a sales team and build a plan for long-term success.

Through my sales leadership career, whether recently promoted or starting with a new team, I have often asked the question: Where do I start?

In the end, I was disappointed with the answers from currently available books and research, left to figure it out myself - which I did over a decade, with great pain and through many transformations. The inability to answer the question – Where do I start? – is why I wrote this book. To answer that question.

The goal of this book is to help sales leaders answer that question by providing a framework to understand the business, build a plan, and guide the team through the different stages of a sales transformation. A framework to succeed at the fastest pace possible, quarter after quarter.

(End back jacket - the rest is just additional context)

Over the last decade, I have had the privilege of leading teams in North America, Europe, and Asia. I have led turnarounds, growth businesses, and realignments. Each team was different in size, complexity, and culture; and each one offered up new and unique challenges. Each team operated with different market dynamics: one was a commodity; one was a low-cost leader; one was a market innovator. Each transformation helped me learn by taking risks, by failing and by succeeding. At each step, I had many teachers; and as I learned, I made notes. Over time I built a framework that you can leverage as you read and absorb this book. As you lead your team through a sales transformation.

I hope that this book will become for you what The Copper Lantern is for me: a favorite on your bookshelf; underlined, highlighted, dog-eared, and an ongoing reference.

Sales leadership is a journey. It is never linear, and it is always changing. At different times, different parts of this book will apply, while others will not, but hopefully, you will find it a useful and long-lasting reference.

Target Market(s)

Business readers. Sales leaders.

Requirements
Must have
• Modern, clear, eye catching colours. Clean. Graphics that indicate growth, leadership, strength.
• Please ensure the design has the full cover and back jacket design. Please use the introduction of the book as the back jacket text.

```html
<!DOCTYPE html>
<html lang="en">
<head>
<meta charset="utf-8">
<title>Guiding Your Revenue Overhaul — Back Jacket</title>
<link href="https://fonts.googleapis.com/css2?family=Libre+Baskerville:wght@700&family=PT+Sans:wght@400&display=swap" rel="stylesheet">
<style>
  :root {
    --page-bg: #f4f1ec;
    --jacket-red: #a5272a;
    --box-red: #9a2326;
    --box-line: #6e1618;
    --band-white: #ededed;
    --ink-light: #ffffff;
    --ink-dark: #1c1212;
    --arrow: #f2f2f2;
    --code-block: #1a1a1a;
  }
  html, body {
    margin: 0;
    padding: 0;
    width: 1200px;
    height: 1200px;
    overflow: hidden;
    background: var(--page-bg);
  }
  .canvas {
    position: relative;
    width: 1200px;
    height: 1200px;
  }
  .jacket {
    position: absolute;
    left: 210px;
    top: 95px;
    width: 780px;
    height: 1010px;
    background: var(--jacket-red);
    box-shadow: 0 6px 18px rgba(0,0,0,0.18);
    overflow: hidden;
  }
  .jacket-title {
    position: absolute;
    left: 0;
    top: 18px;
    width: 100%;
    margin: 0;
    text-align: center;
    font-family: "Libre Baskerville", "Times New Roman", serif;
    font-weight: 700;
    font-size: 44px;
    line-height: 56px;
    color: var(--ink-light);
    letter-spacing: 0.5px;
  }
  .author-box {
    position: absolute;
    left: 22px;
    top: 132px;
    width: 120px;
    height: 120px;
    background: var(--box-red);
    border: 1.5px solid var(--box-line);
    display: flex;
    align-items: center;
    justify-content: center;
    font-family: "PT Sans", Arial, sans-serif;
    font-size: 26px;
    color: var(--ink-dark);
  }
  .pull-quote {
    position: absolute;
    left: 164px;
    top: 138px;
    width: 590px;
    margin: 0;
    font-family: "PT Sans", Arial, sans-serif;
    font-size: 19.5px;
    line-height: 26px;
    color: var(--ink-light);
  }
  .growth-arrow {
    position: absolute;
    left: 56px;
    top: 292px;
    width: 102px;
    height: 566px;
  }
  .blurb {
    position: absolute;
    left: 174px;
    top: 284px;
    width: 580px;
    font-family: "PT Sans", Arial, sans-serif;
    font-size: 18.5px;
    line-height: 25px;
    color: var(--ink-dark);
  }
  .blurb p {
    margin: 0 0 25px 0;
  }
  .blurb p:last-child {
    margin-bottom: 0;
  }
  .base-band {
    position: absolute;
    left: 0;
    bottom: 0;
    width: 100%;
    height: 115px;
    background: var(--band-white);
  }
  .book-name {
    position: absolute;
    left: 26px;
    top: 42px;
    margin: 0;
    font-family: "Libre Baskerville", "Times New Roman", serif;
    font-weight: 700;
    font-size: 22px;
    line-height: 28px;
    color: var(--jacket-red);
  }
  .code-block {
    position: absolute;
    right: 28px;
    bottom: 0;
    width: 211px;
    height: 50px;
    background: var(--code-block);
  }
</style>
</head>
<body>
<main class="canvas">
  <section class="jacket" aria-label="Back jacket">
    <h1 class="jacket-title">A GUIDE FOR NEW SALES<br>LEADERS</h1>

    <div class="author-box">AVARTAR</div>

    <p class="pull-quote">“Sales leadership is a journey. It is never linear, and it is<br>always changing. At different times, different parts of this<br>book will apply, while others will not, but hopefully, you<br>will find it a useful and long-lasting reference”</p>

    <svg class="growth-arrow" viewBox="0 0 102 566" aria-hidden="true">
      <polygon fill="var(--arrow)" points="51,0 102,150 68,150 68,566 34,566 34,150 0,150"/>
    </svg>

    <div class="blurb">
      <p>Sales transformation is a topic that is infrequently written<br>about. For the new sales leader, there are a myriad of<br>books written on coaching, leadership, forecasting, solu-<br>tion selling and sales process but very little is written<br>about how to assess a sales team and build a plan for<br>long-term success.</p>
      <p>Through my sales leadership career, whether recently<br>promoted or starting with a new team, I have often asked<br>the question: Where do I start?</p>
      <p>In the end, I was disappointed with the answers from cur-<br>rently available books and research, left to figure it out<br>myself - which I did over a decade, with great pain and<br>through many transformations. The inability to answer<br>the question – Where do I start? – is why I wrote this<br>book. To answer that question.</p>
      <p>The goal of this book is to help sales leaders answer that<br>question by providing a framework to understand the<br>business, build a plan, and guide the team through the<br>different stages of a sales transformation. A framework to<br>succeed at the fastest pace possible, quarter after quarter.</p>
    </div>

    <div class="base-band">
      <p class="book-name">Guiding Your Revenue Overhaul</p>
      <div class="code-block"></div>
    </div>
  </section>
</main>
</body>
</html>
```